Relocation/furniture installation company needs new business cards

we are a relocation and furniture installation company mainly dealing with corporate clients and we are looking for new business card ideas. Cards should incorporate our logo and list our website, phone number and services. The company is only 2 years old but with more staff joining we are in the need for more business cards, so something with an awesome design that is eye catching would go a long way to insure we get our name out there and look good to potential new clients.

Target Market(s)

Corporate

Industry/Entity Type

Trade

Contact Information for Business Card

www.mervoline.co.nz
0508 4 bravok

furniture installation
business relocations
joinery installation
commercial property maintenance

Colors
0592cd
34a7d8
85cae6
85acd3
0356a4
cfdfed
cee9f5
757575
474747

Requirements
Must have
• Business relocations and furniture installation specialists
Nice to have
• something that incorporates our logo.

```html
<!DOCTYPE html>
<html lang="en">
<head>
<meta charset="utf-8">
<title>Mervoline business cards</title>
<link href="https://fonts.googleapis.com/css2?family=Lato:wght@400;700&display=swap" rel="stylesheet">
<style>
  :root {
    --bg: #3a3a3a;
    --card-white: #ffffff;
    --card-blue: #5596db;
    --navy: #2e3a8f;
    --sky: #1e9ad6;
    --ink: #2a2a2a;
    --light: #ffffff;
  }
  * { box-sizing: border-box; margin: 0; padding: 0; }
  html, body { width: 1200px; height: 900px; overflow: hidden; }
  body {
    background: var(--bg);
    font-family: "Lato", sans-serif;
    position: relative;
  }
  .card {
    position: absolute;
    width: 525px;
    height: 300px;
    overflow: hidden;
    box-shadow: 0 10px 30px rgba(0,0,0,0.45);
  }
  /* back side */
  .card-back {
    left: 610px; top: 110px;
    background: var(--card-blue);
    color: var(--light);
  }
  .card-back .brand {
    position: absolute;
    left: 0; right: 0; top: 92px;
    text-align: center;
    font-size: 48px;
    font-weight: 700;
    letter-spacing: 6px;
    color: var(--light);
  }
  .card-back .services {
    position: absolute;
    left: 0; right: 0; top: 175px;
    text-align: center;
    font-size: 13px;
    letter-spacing: 0.5px;
    line-height: 1.55;
    text-transform: uppercase;
  }
  /* front side */
  .card-front {
    left: 75px; top: 480px;
    background: var(--card-white);
    color: var(--ink);
  }
  .card-front .swoosh {
    position: absolute; left: 0; top: 0;
    width: 525px; height: 300px;
  }
  .card-front .brand {
    position: absolute;
    left: 34px; top: 30px;
    font-size: 40px;
    font-weight: 700;
    letter-spacing: 5px;
    color: var(--navy);
  }
  .card-front .address {
    position: absolute;
    left: 36px; top: 92px;
    font-size: 13px;
    line-height: 1.4;
  }
  .card-front .contacts {
    position: absolute;
    left: 36px; top: 134px;
    list-style: none;
    font-size: 13px;
    line-height: 1.55;
  }
  .card-front .contacts li { display: flex; align-items: center; gap: 7px; }
  .card-front .contacts svg { width: 11px; height: 11px; }
  .card-front .icon-phone { fill: var(--sky); }
  .card-front .icon-mail { fill: none; stroke: var(--sky); stroke-width: 2.5; }
  .card-front .person {
    position: absolute;
    right: 38px; top: 150px;
    text-align: left;
  }
  .card-front .person-name {
    font-size: 23px;
    font-weight: 700;
    color: var(--sky);
  }
  .card-front .person-role { font-size: 13px; color: var(--ink); }
  .card-front .website {
    position: absolute;
    left: 48px; bottom: 14px;
    font-size: 15px;
    color: var(--light);
  }
</style>
</head>
<body>
  <section class="card card-back">
    <div class="brand">MERVOLINE</div>
    <p class="services">
      Furniture installation • Business relocations<br>
      Joinery installation • Commercial property maintenance
    </p>
  </section>

  <section class="card card-front">
    <svg class="swoosh" viewBox="0 0 525 300" aria-hidden="true">
      <path d="M0 190 C150 242 330 264 525 266 L525 300 L0 300 Z" fill="#2e3a8f"/>
      <path d="M0 198 C150 250 330 271 525 273 L525 300 L0 300 Z" fill="#ffffff"/>
      <path d="M0 204 C150 256 330 277 525 279 L525 300 L0 300 Z" fill="#5596db"/>
    </svg>
    <div class="brand">MERVOLINE</div>
    <p class="address">148 Harbour Row<br>Tauranga 3110</p>
    <ul class="contacts">
      <li><svg class="icon-phone" viewBox="0 0 24 24"><path d="M6.6 10.8a15 15 0 0 0 6.6 6.6l2.2-2.2c.3-.3.7-.4 1-.2 1.1.4 2.3.6 3.6.6.6 0 1 .4 1 1V20c0 .6-.4 1-1 1A17 17 0 0 1 3 4c0-.6.4-1 1-1h3.5c.6 0 1 .4 1 1 0 1.3.2 2.5.6 3.6.1.3 0 .7-.2 1z"/></svg>0508 4 bravok</li>
      <li><svg class="icon-mail" viewBox="0 0 24 24"><path d="M2 5h20v14H2z M2 5l10 8 10-8"/></svg>info@mervoline.co.nz</li>
    </ul>
    <div class="person">
      <div class="person-name">Daniel Corwen</div>
      <div class="person-role">Manager</div>
    </div>
    <div class="website">www.mervoline.co.nz</div>
  </section>
</body>
</html>
```